Letterhead

Create letterhead for corporate letters, proposals, thank yous, etc.

Target Market(s)

Technology, Communications

Industry/Entity Type

Information Technology

```html
<!DOCTYPE html>
<html lang="en">
<head>
<meta charset="utf-8">
<title>Stratum Nine Letterhead</title>
<link rel="stylesheet" href="https://fonts.googleapis.com/css2?family=Questrial&display=swap">
<style>
  :root {
    --paper: #ffffff;
    --brand-grey: #6f7f8a;
    --sky-light: #d3e8f3;
    --sky-mid: #8fc3df;
    --sky-deep: #3d8fc4;
    --ocean: #1f74b4;
    --shadow-grey: #c9ced2;
  }
  * { margin: 0; padding: 0; box-sizing: border-box; }
  html, body { width: 849px; height: 1200px; overflow: hidden; background: var(--paper); }
  .letterhead { position: relative; width: 849px; height: 1200px; background: var(--paper); overflow: hidden; }
  .header-band, .footer-band, .centre-decoration { position: absolute; left: 0; display: block; }
  .header-band { top: 0; }
  .footer-band { bottom: 0; }
  .centre-decoration { left: 170px; top: 320px; }
  .brand {
    position: absolute; left: 50px; top: 82px;
    display: flex; align-items: center; gap: 12px;
    font-family: "Questrial", sans-serif; font-size: 38px; line-height: 1;
    color: var(--brand-grey); letter-spacing: 0.5px;
  }
  .brand-dot { width: 28px; height: 28px; border-radius: 50%; background: var(--brand-grey); }
</style>
</head>
<body>
<main class="letterhead">
  <svg class="header-band" width="849" height="320" viewBox="0 0 849 320">
    <defs>
      <linearGradient id="header-photo-tone" x1="0" y1="0" x2="1" y2="0.4">
        <stop offset="0" stop-color="#e3f0f7"/>
        <stop offset="0.5" stop-color="#a9d0e6"/>
        <stop offset="1" stop-color="#d7e6ee"/>
      </linearGradient>
    </defs>
    <path d="M0 0 H849 V160 C700 150 520 190 360 240 C220 285 90 300 0 296 Z" fill="var(--shadow-grey)"/>
    <path role="img" aria-label="Faded blue-toned photograph of people at work in a bright office" d="M0 0 H849 V150 C700 140 520 178 360 226 C220 270 90 286 0 282 Z" fill="url(#header-photo-tone)"/>
  </svg>

  <div class="brand"><span class="brand-dot"></span><span class="brand-name">Stratum Nine</span></div>

  <svg class="centre-decoration" width="500" height="460" viewBox="0 0 500 460">
    <defs>
      <linearGradient id="centre-tone" x1="0" y1="1" x2="1" y2="0">
        <stop offset="0" stop-color="#e4f1f8"/>
        <stop offset="0.6" stop-color="#c3e0ef"/>
        <stop offset="1" stop-color="#dcdfe1"/>
      </linearGradient>
    </defs>
    <ellipse role="img" aria-label="Pale blue and grey decorative arc pattern" cx="250" cy="230" rx="230" ry="120" transform="rotate(-40 250 230)" fill="url(#centre-tone)"/>
  </svg>

  <svg class="footer-band" width="849" height="190" viewBox="0 0 849 190">
    <defs>
      <linearGradient id="footer-tone" x1="0" y1="0" x2="0" y2="1">
        <stop offset="0" stop-color="var(--sky-light)"/>
        <stop offset="0.5" stop-color="var(--sky-mid)"/>
        <stop offset="1" stop-color="var(--ocean)"/>
      </linearGradient>
    </defs>
    <path d="M0 20 C200 0 420 10 620 40 C720 55 800 62 849 60 V190 H0 Z" fill="var(--shadow-grey)"/>
    <path role="img" aria-label="Blue decorative wave pattern" d="M0 34 C200 14 420 24 620 54 C720 69 800 76 849 74 V190 H0 Z" fill="url(#footer-tone)"/>
  </svg>
</main>
</body>
</html>
```